LEARN Business Skills so you can Earn a good living

size of the poster is 8”x 10.75" plus 0.25" bleed.
Please leave 1 inch on the bottoum for footer
I want a design a poster that will attract people's attention.
I appreciate a creative ad however the ad should not take away from being able to clearly read the text.
-I also appreciate a simple creative ad that is not too busy.
-you can use graphics, vectors, or pictures of real people.
-however, if you use real people it should be a white male that is wearing a white shirt and look like a professional person.

Target Market(s)

Potential young business people

Industry/Entity Type

education

Requirements
Must have
• easy to read the text
Nice to have
• I would like a "creative" simple ad that is easy to be read
Should not have
• pictures of women

```html
<!DOCTYPE html>
<html lang="en">
<head>
<meta charset="utf-8">
<title>Learn to Earn – Business Enrichment Course</title>
<link href="https://fonts.googleapis.com/css2?family=Archivo:wght@400;500;600;700;800&family=Montserrat:wght@500;600;700&display=swap" rel="stylesheet">
<style>
  :root{
    --navy:#173a52;
    --navy-deep:#102c40;
    --teal:#1d5a74;
    --orange:#f6a21c;
    --white:#ffffff;
    --ink:#1f2a33;
    --grey-line:#9aa6ae;
    --backdrop:#e9e7e3;
  }
  *{box-sizing:border-box;margin:0;padding:0}
  html,body{width:1051px;height:1200px;overflow:hidden}
  body{background:var(--backdrop);font-family:"Archivo",Arial,sans-serif;color:var(--ink)}

  .poster{
    position:absolute;left:95px;top:22px;width:860px;height:1156px;
    background:var(--white);overflow:hidden;
    box-shadow:0 4px 18px rgba(0,0,0,.15);
  }

  .hero-photo{
    position:absolute;left:0;top:0;width:860px;height:720px;
    background:
      radial-gradient(ellipse 260px 420px at 640px 360px,#5b4a42 0%,#8a7e78 35%,rgba(160,170,178,0) 75%),
      linear-gradient(90deg,#b9c0c6 0%,#a7b1b9 40%,#c9d2d9 70%,#d8dfe4 100%);
  }
  .hero-fade{
    position:absolute;left:0;top:0;width:860px;height:720px;
    background:linear-gradient(90deg,rgba(255,255,255,.92) 0%,rgba(255,255,255,.7) 30%,rgba(255,255,255,0) 55%);
  }

  .headline{position:absolute;left:48px;top:54px;line-height:.86;letter-spacing:-2px}
  .headline .learn{color:var(--navy);font-weight:800;font-size:132px}
  .headline .to{color:var(--navy);font-weight:500;font-size:104px;letter-spacing:-1px;margin-left:8px}
  .headline .earn{display:block;color:var(--orange);font-weight:800;font-size:132px;margin-top:6px}

  .course-band{
    position:absolute;left:0;top:340px;width:520px;padding:22px 30px 26px 48px;
    background:rgba(23,58,82,.92);color:var(--white);
  }
  .course-band h2{color:var(--orange);font-family:"Montserrat",Arial,sans-serif;font-weight:700;font-size:32px;line-height:1.1}
  .course-band p{font-family:"Montserrat",Arial,sans-serif;font-weight:500;font-size:21px;line-height:1.3;margin-top:8px}

  .lower-panel{position:absolute;left:0;top:600px;width:860px;height:556px}

  .benefits{position:absolute;left:0;top:585px;width:860px;display:flex;justify-content:space-around;padding:0 60px}
  .benefit{width:220px;text-align:center;position:relative}
  .benefit + .benefit::before{
    content:"";position:absolute;left:-22px;top:70px;height:100px;border-left:2px dotted var(--grey-line);
  }
  .benefit-icon{
    width:104px;height:104px;margin:0 auto;border-radius:50%;
    background:var(--navy);border:6px solid #e6eaed;display:flex;align-items:center;justify-content:center;
  }
  .benefit-label{margin-top:12px;font-family:"Montserrat",Arial,sans-serif;font-weight:500;font-size:19px;line-height:1.2;color:var(--ink)}

  .topics{position:absolute;left:40px;top:872px;width:790px;display:grid;grid-template-columns:245px 185px 215px 125px;column-gap:6px}
  .topics ul{list-style:none}
  .topics li{display:flex;align-items:center;gap:7px;font-family:"Montserrat",Arial,sans-serif;font-weight:600;font-size:14px;line-height:1;margin-bottom:15px;color:var(--ink);white-space:nowrap}
  .tick{width:13px;height:13px;flex:none}

  .footer-band{
    position:absolute;left:0;bottom:0;width:860px;height:103px;
    background:linear-gradient(180deg,var(--teal) 0%,var(--navy-deep) 100%);
  }
</style>
</head>
<body>
<div class="poster">
  <div class="hero-photo" role="img" aria-label="Photo of a young professional in a white shirt and tie seated in a bright classroom"></div>
  <div class="hero-fade"></div>

  <h1 class="headline"><span class="learn">LEARN</span><span class="to">to</span><span class="earn">EARN</span></h1>

  <div class="course-band">
    <h2>Business Enrichment Course</h2>
    <p>A proven success of helping people in their livelihoods Business skills that will help you:</p>
  </div>

  <svg class="lower-panel" viewBox="0 0 860 556" aria-hidden="true">
    <defs>
      <linearGradient id="panelFade" x1="0" y1="0" x2="0" y2="1">
        <stop offset="0" stop-color="#f1f3f5"/>
        <stop offset="0.25" stop-color="#ffffff"/>
        <stop offset="0.78" stop-color="#ffffff"/>
        <stop offset="0.84" stop-color="#c9d6dd"/>
        <stop offset="0.88" stop-color="#1d5a74"/>
        <stop offset="1" stop-color="#102c40"/>
      </linearGradient>
    </defs>
    <path d="M0 150 Q430 20 860 60 L860 556 L0 556 Z" fill="url(#panelFade)"/>
  </svg>

  <div class="benefits">
    <div class="benefit" style="margin-top:80px">
      <div class="benefit-icon">
        <svg width="56" height="56" viewBox="0 0 56 56" aria-hidden="true">
          <rect x="8" y="18" width="40" height="28" rx="3" fill="var(--orange)"/>
          <rect x="20" y="10" width="16" height="10" rx="2" fill="none" stroke="var(--orange)" stroke-width="4"/>
          <rect x="8" y="28" width="40" height="3" fill="var(--navy)"/>
        </svg>
      </div>
      <div class="benefit-label">Get a<br>quality job</div>
    </div>
    <div class="benefit" style="margin-top:40px">
      <div class="benefit-icon">
        <svg width="58" height="58" viewBox="0 0 58 58" aria-hidden="true">
          <rect x="8" y="34" width="7" height="16" fill="var(--orange)"/>
          <rect x="19" y="28" width="7" height="22" fill="var(--orange)"/>
          <rect x="30" y="22" width="7" height="28" fill="var(--orange)"/>
          <rect x="41" y="14" width="7" height="36" fill="var(--orange)"/>
          <path d="M6 26 L20 16 L30 20 L46 6" fill="none" stroke="var(--orange)" stroke-width="3"/>
          <path d="M40 5 L48 5 L48 13" fill="none" stroke="var(--orange)" stroke-width="3"/>
        </svg>
      </div>
      <div class="benefit-label">Start/grow<br>your business</div>
    </div>
    <div class="benefit" style="margin-top:0">
      <div class="benefit-icon">
        <svg width="56" height="56" viewBox="0 0 56 56" aria-hidden="true">
          <path d="M8 44 L22 30 L30 36 L46 18" fill="none" stroke="var(--orange)" stroke-width="5" stroke-linejoin="round"/>
          <path d="M38 16 L48 16 L48 26" fill="none" stroke="var(--orange)" stroke-width="5"/>
          <text x="30" y="16" font-family="Archivo,Arial,sans-serif" font-weight="800" font-size="18" fill="var(--orange)">$</text>
        </svg>
      </div>
      <div class="benefit-label">Increase<br>your salary</div>
    </div>
  </div>

  <div class="topics">
    <ul>
      <li><svg class="tick" viewBox="0 0 13 13"><rect x=".75" y=".75" width="11.5" height="11.5" fill="none" stroke="var(--navy)" stroke-width="1.5"/><path d="M3 6.5 L5.5 9 L10 3.5" fill="none" stroke="var(--navy)" stroke-width="1.6"/></svg>Business Administration</li>
      <li><svg class="tick" viewBox="0 0 13 13"><rect x=".75" y=".75" width="11.5" height="11.5" fill="none" stroke="var(--navy)" stroke-width="1.5"/><path d="M3 6.5 L5.5 9 L10 3.5" fill="none" stroke="var(--navy)" stroke-width="1.6"/></svg>Small Business Management</li>
      <li><svg class="tick" viewBox="0 0 13 13"><rect x=".75" y=".75" width="11.5" height="11.5" fill="none" stroke="var(--navy)" stroke-width="1.5"/><path d="M3 6.5 L5.5 9 L10 3.5" fill="none" stroke="var(--navy)" stroke-width="1.6"/></svg>Health Care Management</li>
      <li><svg class="tick" viewBox="0 0 13 13"><rect x=".75" y=".75" width="11.5" height="11.5" fill="none" stroke="var(--navy)" stroke-width="1.5"/><path d="M3 6.5 L5.5 9 L10 3.5" fill="none" stroke="var(--navy)" stroke-width="1.6"/></svg>Investments</li>
      <li><svg class="tick" viewBox="0 0 13 13"><rect x=".75" y=".75" width="11.5" height="11.5" fill="none" stroke="var(--navy)" stroke-width="1.5"/><path d="M3 6.5 L5.5 9 L10 3.5" fill="none" stroke="var(--navy)" stroke-width="1.6"/></svg>Computers</li>
    </ul>
    <ul>
      <li><svg class="tick" viewBox="0 0 13 13"><rect x=".75" y=".75" width="11.5" height="11.5" fill="none" stroke="var(--navy)" stroke-width="1.5"/><path d="M3 6.5 L5.5 9 L10 3.5" fill="none" stroke="var(--navy)" stroke-width="1.6"/></svg>Accounting</li>
      <li><svg class="tick" viewBox="0 0 13 13"><rect x=".75" y=".75" width="11.5" height="11.5" fill="none" stroke="var(--navy)" stroke-width="1.5"/><path d="M3 6.5 L5.5 9 L10 3.5" fill="none" stroke="var(--navy)" stroke-width="1.6"/></svg>Sales Marketing</li>
      <li><svg class="tick" viewBox="0 0 13 13"><rect x=".75" y=".75" width="11.5" height="11.5" fill="none" stroke="var(--navy)" stroke-width="1.5"/><path d="M3 6.5 L5.5 9 L10 3.5" fill="none" stroke="var(--navy)" stroke-width="1.6"/></svg>Project Management</li>
      <li><svg class="tick" viewBox="0 0 13 13"><rect x=".75" y=".75" width="11.5" height="11.5" fill="none" stroke="var(--navy)" stroke-width="1.5"/><path d="M3 6.5 L5.5 9 L10 3.5" fill="none" stroke="var(--navy)" stroke-width="1.6"/></svg>Interviewing Skills</li>
      <li><svg class="tick" viewBox="0 0 13 13"><rect x=".75" y=".75" width="11.5" height="11.5" fill="none" stroke="var(--navy)" stroke-width="1.5"/><path d="M3 6.5 L5.5 9 L10 3.5" fill="none" stroke="var(--navy)" stroke-width="1.6"/></svg>Business Law</li>
    </ul>
    <ul>
      <li><svg class="tick" viewBox="0 0 13 13"><rect x=".75" y=".75" width="11.5" height="11.5" fill="none" stroke="var(--navy)" stroke-width="1.5"/><path d="M3 6.5 L5.5 9 L10 3.5" fill="none" stroke="var(--navy)" stroke-width="1.6"/></svg>Negotiation</li>
      <li><svg class="tick" viewBox="0 0 13 13"><rect x=".75" y=".75" width="11.5" height="11.5" fill="none" stroke="var(--navy)" stroke-width="1.5"/><path d="M3 6.5 L5.5 9 L10 3.5" fill="none" stroke="var(--navy)" stroke-width="1.6"/></svg>Public Speaking</li>
      <li><svg class="tick" viewBox="0 0 13 13"><rect x=".75" y=".75" width="11.5" height="11.5" fill="none" stroke="var(--navy)" stroke-width="1.5"/><path d="M3 6.5 L5.5 9 L10 3.5" fill="none" stroke="var(--navy)" stroke-width="1.6"/></svg>Import/export</li>
      <li><svg class="tick" viewBox="0 0 13 13"><rect x=".75" y=".75" width="11.5" height="11.5" fill="none" stroke="var(--navy)" stroke-width="1.5"/><path d="M3 6.5 L5.5 9 L10 3.5" fill="none" stroke="var(--navy)" stroke-width="1.6"/></svg>Information Technology</li>
      <li><svg class="tick" viewBox="0 0 13 13"><rect x=".75" y=".75" width="11.5" height="11.5" fill="none" stroke="var(--navy)" stroke-width="1.5"/><path d="M3 6.5 L5.5 9 L10 3.5" fill="none" stroke="var(--navy)" stroke-width="1.6"/></svg>Distribution</li>
    </ul>
    <ul>
      <li><svg class="tick" viewBox="0 0 13 13"><rect x=".75" y=".75" width="11.5" height="11.5" fill="none" stroke="var(--navy)" stroke-width="1.5"/><path d="M3 6.5 L5.5 9 L10 3.5" fill="none" stroke="var(--navy)" stroke-width="1.6"/></svg>Marketing</li>
      <li><svg class="tick" viewBox="0 0 13 13"><rect x=".75" y=".75" width="11.5" height="11.5" fill="none" stroke="var(--navy)" stroke-width="1.5"/><path d="M3 6.5 L5.5 9 L10 3.5" fill="none" stroke="var(--navy)" stroke-width="1.6"/></svg>LedgerLite</li>
      <li><svg class="tick" viewBox="0 0 13 13"><rect x=".75" y=".75" width="11.5" height="11.5" fill="none" stroke="var(--navy)" stroke-width="1.5"/><path d="M3 6.5 L5.5 9 L10 3.5" fill="none" stroke="var(--navy)" stroke-width="1.6"/></svg>Real Estate</li>
      <li><svg class="tick" viewBox="0 0 13 13"><rect x=".75" y=".75" width="11.5" height="11.5" fill="none" stroke="var(--navy)" stroke-width="1.5"/><path d="M3 6.5 L5.5 9 L10 3.5" fill="none" stroke="var(--navy)" stroke-width="1.6"/></svg>Finance</li>
      <li><svg class="tick" viewBox="0 0 13 13"><rect x=".75" y=".75" width="11.5" height="11.5" fill="none" stroke="var(--navy)" stroke-width="1.5"/><path d="M3 6.5 L5.5 9 L10 3.5" fill="none" stroke="var(--navy)" stroke-width="1.6"/></svg>Shopvale</li>
    </ul>
  </div>

  <div class="footer-band"></div>
</div>
</body>
</html>
```